Brochure Design

Hello,

The brief requirements have changed:

We are a printing company based in Singapore & Las Vegas. We specialize in blue-print printing for the Architectural, Engineering and Construction industries.

Our website is www.tvkholdings.net where you can find more information on our company and services

The design should be simple, professional, clean and organized.

Pantone colors that we use for our company:

Orange: PMS 021
Gray: PMS 431

Attachments are as follows:

• Company logos.
• Existing brochure that are trying to improve on.
• Other existing fliers for reference that includes some of the information that we would like to incorporate into the brochure.

Some of the things we would like incorporated into the design:

• A3 2-sided brochure (A4 pages 1-4) that will be folded in half
• Ideally we would like the ability to take each A4 page and use it individually which means the that each page could be separated from the brochure and used on its own if required.
• We would like the template of the design to be changeable and have the ability to change/add information & services in the future, but keep the main design of the brochure intact.

Considering we have two locations on different continents, we need a template where the address details to be interchangeable for each different location.

• TVK Singapore – TVK Lumaplex Services Pte Ltd

• TVK Las Vegas – TVK Lumaplex Services

This is the first time we have requested for a brochure to be created so please let me know if you require any additional information.

Thank you.

Target Market(s)

Architects, Engineering Firms and Construction Companies.

Industry/Entity Type

Printing

Font styles to use
Other font styles liked:
• Times New Roman

Colors

Designer to choose colors to be used in the design.

Requirements
Must have
• Please use the Font, Times New Roman only.
Should not have
• Any playful art or graphic printing related images or logos.

```html
<!DOCTYPE html>
<html lang="en">
<head>
<meta charset="utf-8">
<title>TVK Lumaplex Services Brochure</title>
<link href="https://fonts.googleapis.com/css2?family=Tinos:ital,wght@0,400;0,700;1,400;1,700&display=swap" rel="stylesheet">
<style>
:root{
  --orange:#ff3c14;
  --orange-soft:#ff8560;
  --ink:#111;
  --white:#fff;
  --page-border:#d9d9d9;
}
*{margin:0;padding:0;box-sizing:border-box}
html,body{width:1200px;height:849px;overflow:hidden;background:var(--white)}
body{font-family:"Tinos","Times New Roman",serif;color:var(--ink);position:relative}
.page{position:absolute;top:0;width:600px;height:849px;overflow:hidden}
.page--evolution{left:0;background:var(--white);border:1px solid var(--page-border)}
.page--intro{left:600px;background:var(--orange);color:var(--white)}
.shape{position:absolute;left:0;top:0}
.masthead{position:absolute;top:52px;left:0;width:600px;text-align:center}
.masthead__name{font-size:44px;font-weight:400;letter-spacing:1px;line-height:48px}
.masthead__title{font-size:20px;font-weight:700;margin-top:6px}
.masthead__title em{font-style:italic}
.masthead__member{font-size:14px;font-weight:700;font-style:italic;margin-top:1px}
.masthead__locations{font-size:13px;font-weight:700;margin-top:14px}
.page--intro .masthead__name,.page--intro .masthead__title,.page--intro .masthead__member,.page--intro .masthead__locations{color:var(--ink)}
.section-title{position:absolute;top:284px;font-size:16px;letter-spacing:1.2px;font-weight:400}
.page--evolution .section-title{left:88px}
.page--intro .section-title{left:185px;color:var(--white)}
.feature{position:absolute;left:88px;width:430px;display:flex;align-items:flex-start;gap:22px}
.feature__icon{flex:0 0 42px;height:42px}
.feature__text{font-size:10px;line-height:11.6px;text-align:justify}
.contacts{position:absolute;top:783px;left:0;width:600px;display:flex;color:var(--ink);font-size:8.4px;line-height:10.6px;text-align:center}
.contact{position:absolute;width:280px}
.contact--sg{left:25px}.contact--lv{left:330px}
.contact__label{letter-spacing:.3px}
.contact__company{font-weight:700}
.side-title{position:absolute;left:72px;top:720px;transform:rotate(-90deg);transform-origin:0 0;color:var(--orange-soft);font-weight:700;font-size:44px;line-height:46px;letter-spacing:4px;white-space:nowrap}
.intro-body{position:absolute;left:186px;top:321px;width:365px;font-size:9.9px;line-height:11.4px;text-align:justify}
.intro-body p{margin-bottom:11.4px}
.website{position:absolute;left:364px;top:812px;color:var(--orange);font-size:16px}
</style>
</head>
<body>

<section class="page page--evolution">
  <svg class="shape" width="600" height="849" viewBox="0 0 600 849" aria-hidden="true">
    <path d="M44 201 Q300 262 556 201 Q300 245 44 201 Z" fill="var(--orange)"/>
    <path d="M0 740 Q300 770 600 750 L600 849 L0 849 Z" fill="var(--orange)"/>
  </svg>

  <header class="masthead">
    <div class="masthead__name">TVK</div>
    <div class="masthead__title">TVK Lumaplex Services</div>
    <div class="masthead__member">A Member of the TVK Group of Companies</div>
    <div class="masthead__locations">Singapore | Las Vegas</div>
  </header>

  <h2 class="section-title">THE EVOLUTION OF TVK LUMAPLEX SERVICES</h2>

  <div class="feature" style="top:322px">
    <svg class="feature__icon" viewBox="0 0 42 42" role="img" aria-label="Talent icon"><circle cx="21" cy="21" r="20" fill="var(--orange)"/></svg>
    <p class="feature__text">TVK Lumaplex Services (TVK) is constantly enhancing its organization through recruitment, training and developing “Human Talent” that can fully share the creativity and the passions……. “The Difference”……that contributes to the growth, success and evolution of TVK.</p>
  </div>
  <div class="feature" style="top:385px">
    <svg class="feature__icon" viewBox="0 0 42 42" role="img" aria-label="Colour printing icon"><circle cx="21" cy="21" r="20" fill="#222"/><path d="M21 1 A20 20 0 0 0 1 21 L21 21 Z" fill="#e6007e"/><path d="M21 1 A20 20 0 0 1 41 21 L21 21 Z" fill="#ffd800"/><path d="M1 21 A20 20 0 0 0 21 41 L21 21 Z" fill="#00a0e3"/></svg>
    <p class="feature__text">TVK has become Singapore’s leading Digital Repro<i>Graphic</i>, Colour Printing and Specialty Book Making Provider. From the onset, it has always been our intention to provide new and innovative technology solutions whilst maintaining exceptional service standards to our customers. Hence, our operation at Tannery Road.</p>
  </div>
  <div class="feature" style="top:451px">
    <svg class="feature__icon" viewBox="0 0 42 42" role="img" aria-label="24 hour service icon"><circle cx="21" cy="21" r="19" fill="none" stroke="var(--orange)" stroke-width="3"/><rect x="6" y="15" width="30" height="13" rx="2" fill="var(--orange)"/></svg>
    <p class="feature__text">As the largest Repro<i>Graphic</i> company in Singapore, we are dedicated in providing unprecedented standards of customer service, an unrivaled “Can do attitude” including 24 hour service operation, a managed fleet of dedicated dispatch rider and transit vans throughout Singapore.</p>
  </div>
  <div class="feature" style="top:515px">
    <svg class="feature__icon" viewBox="0 0 42 42" role="img" aria-label="Quality icon"><circle cx="21" cy="17" r="15" fill="none" stroke="#222" stroke-width="2"/><circle cx="21" cy="17" r="10" fill="var(--orange)"/><path d="M13 29 L9 40 L17 36 Z M29 29 L33 40 L25 36 Z" fill="var(--orange)"/></svg>
    <p class="feature__text">We are fully committed to providing the highest quality digital output and professional service to make each project a success and more importantly, at a cost that meets your budget.</p>
  </div>
  <div class="feature" style="top:581px">
    <svg class="feature__icon" viewBox="0 0 42 42" role="img" aria-label="Growth icon"><circle cx="21" cy="21" r="16" fill="var(--orange)"/><path d="M13 28 L19 22 L23 25 L30 15" fill="none" stroke="#fff" stroke-width="2"/></svg>
    <p class="feature__text">Furthermore, we will continue to focus on a “Second to none” customer service strategy to ensure your expectations are always exceeded.</p>
  </div>
  <div class="feature" style="top:634px">
    <svg class="feature__icon" viewBox="0 0 42 42" role="img" aria-label="Consultation icon"><circle cx="21" cy="21" r="20" fill="var(--orange)"/><rect x="10" y="23" width="22" height="3" fill="#fff"/></svg>
    <p class="feature__text">Our philosophy is to take the time to consult and understand each of our client’s needs and recognizing the unique requirements of each project and deadline.</p>
  </div>

  <footer class="contacts">
    <div class="contact contact--sg">
      <div class="contact__label">SINGAPORE OFFICE</div>
      <div class="contact__company">TVK Lumaplex Services Pte Ltd</div>
      <div>28 Tannery Road #05-02 to #05-06, Singapore 347719</div>
      <div>Tel : +65 6480-2273 &nbsp;Email : customerservice.sg@tvkholdings.net</div>
    </div>
    <div class="contact contact--lv">
      <div class="contact__label">LAS VEGAS OFFICE</div>
      <div class="contact__company">TVK Lumaplex Services</div>
      <div>4870 W. Sunset Rd, Suite 204, Las Vegas, NV 89118</div>
      <div>Tel : (702) 555-0147 &nbsp;Email : customerservice.lv@tvkholdings.net</div>
    </div>
  </footer>
</section>

<section class="page page--intro">
  <svg class="shape" width="600" height="849" viewBox="0 0 600 849" aria-hidden="true">
    <path d="M42 201 Q300 240 556 201 Q300 228 42 201 Z" fill="var(--white)"/>
    <path d="M0 745 Q300 790 600 738 L600 849 L0 849 Z" fill="var(--white)"/>
  </svg>

  <header class="masthead">
    <div class="masthead__name">TVK</div>
    <div class="masthead__title">TVK Lumaplex Services</div>
    <div class="masthead__member">A Member of the TVK Group of Companies</div>
    <div class="masthead__locations">Singapore | Las Vegas</div>
  </header>

  <h2 class="section-title">GENERAL &nbsp;INTRODUCTION</h2>

  <div class="side-title">GENERAL<br>INTRODUCTION</div>

  <div class="intro-body">
    <p>TVK Lumaplex Services Pte Ltd has been established in Singapore since June 2001 during which time the company has constantly strived to develop its business strategy and market position by enhancing and investing into new technology and human resources in order to meet the increasing demands of our valuable customers.</p>
    <p>Our international management team fully understands the only true differentiator is that of the TVK Team delivering “Exceptional Customer Service” Several years of experience in service associated, rlated markets and industries throughout the United Kingdom, USA, Hong Kong and now of course Singapore has taught us that no two customers are alike and therefore, requirements must be assessed and managed on an individual basis in order to succeed in establishing a mutually beneficial and rewarding business partnership.</p>
    <p>Furthermore, the directors and management at TVK understands the dynamics, changes and challenges being sought throughout the industry and the increasing demands of secure high speed digital transmitting of documents, drawing, images and the necessity in providing our customers with quality, professional presentation graphics and colour printing.</p>
    <p>Since our inception, we have continuously led the market in providing unprecedented standards of customer service a “can do attitude” including a 24 hour service operation, a managed fleet of dedicated dispatch riders and transit vans throughout Singapore and introduction of secure, online digital print and ordering software, File Relay Direct (FRD) to name but just a few.</p>
    <p>We recognize and appreciate the importance and the integral role that our customers/business partners have played, inspiring us to invest and expand our business.</p>
    <p>We will continue to introduce the latest technology, innovative and cost effective repro<i>graphic</i> solutions to Singapore, thereby enabling all of its customers the benefit and efficiencies of leveraging on our own investments and enhanced product/service offering.</p>
  </div>

  <div class="website">Website : www.tvkholdings.net</div>
</section>

</body>
</html>
```